Bright Path Flyer Design for Virtual Online Clinic. -5.5 x 8.5 inches (half sheet)

We need a clean, modern flyer design for Bright Path, a new virtual walk-in clinic based in British Columbia. The flyer will be used in libraries, pharmacies, and community centers to help residents easily access primary care through their Bright Path NFC access card.
The flyer will ask a question : NEED A DOCTOR? This should be large and attention grabbing.
The design should clearly feature a Bright Path card image (the access card) as the centerpiece and visually show how patients can use it to book appointments. The tone should feel trustworthy, healthcare-oriented, and community-friendly — clean fonts, clear spacing, and strong readability from a distance.

Side One: This card has the NFC Access Card.
NEED A DOCTOR? (Large Font, Attention Grabbing)
How to Book an Appointment using your Bright Path Card
Step 1: Tap Your Card on Your Phone
Hold your card near the back of your phone.
It will activate automatically — no app needed.
The Bright Path scheduler will open.
Step 2: Schedule Your Appointment
Select your clinical concern.
Choose your time window.
Register (only once).
Confirm your appointment.
Step 3: Relax, we’ll take care of the rest
A doctor will call during your scheduled time.
Once booked, you’ll be able to call our office.
No emails, no texts — just a real person.
It’s that simple.
Side Two:
About Bright Path
Created by Dr. Marcus Ferrigan
Bright Path was founded to make healthcare simple and convenient. Prescription renewals. Common infections. Medical notes. And so much more.
Our doctors can address 120+ health concerns virtually — providing quality care without the waiting room. No waiting rooms. Just real doctors providing real care.
Why Patients Choose Bright Path
Easy access – book and be seen from anywhere in BC.
Effortless booking – tap your Bright Path Card to begin.
Trusted physicians – every visit is with a licensed BC family doctor.
How It Works
Book your visit — choose a time window that fits your day.
Join the queue — you’ll be called when it’s your turn.
Speak directly with your doctor — simple, secure, and stress-free.
Convenient Care for Common Concerns

Additional Details.
Please find the domain to be launched soon. I've attached the NFC card file for review, it is 85.5 mm x 54 mm. The card will be glued to the flyer.
I've attached examples of flyers but they are not the look I am seeking and I am looking for creative solutions.
Thank you!
http://brightpath-example.test/

Adult Patients in British Columbia

Healthcare

• Looking for clean lines, uniform appearance, and high legibility i.e poppins

0054AA
0677BA
7BADD7
CADEEF
E8F1F8

• Need A Doctor?
• Elegant style, not too busy, clear layout.
• Clutter, look cheap - review examples.

```html
<!DOCTYPE html>
<html lang="en">
<head>
<meta charset="utf-8">
<title>Bright Path Flyer – Front and Back</title>
<link href="https://fonts.googleapis.com/css2?family=Bebas+Neue&family=Poppins:wght@400;500;600&display=swap" rel="stylesheet">
<style>
:root{
  --bg:#c6c6c6;
  --navy:#26428c;
  --navy-deep:#1f3a80;
  --wave:#8fa8de;
  --ice:#cadeef;
  --mist:#e8f1f8;
  --grey-box:#e3e3e3;
  --ink:#1c1c1c;
  --white:#ffffff;
}
*{margin:0;padding:0;box-sizing:border-box}
html,body{width:1200px;height:973px;overflow:hidden;background:var(--bg)}
body{position:relative;font-family:"Poppins",sans-serif;color:var(--ink)}
.page{position:absolute;top:181px;width:396px;height:612px;background:var(--white);overflow:hidden}
.page--front{left:191px}
.page--back{left:613px}
.abs{position:absolute}
.head{font-family:"Bebas Neue",sans-serif;line-height:1;letter-spacing:.2px}
.waves{position:absolute;left:0;top:0;width:396px;height:612px}

/* front */
.photo{position:absolute}
.front-photo{left:8px;top:6px;width:143px;height:200px;background:linear-gradient(180deg,#f1f1f1 0%,#e6e9ef 60%,#cfd6e6 100%);border-radius:60px 60px 0 0}
.nfc-note{left:163px;top:15px;color:var(--white);font-size:15px;white-space:nowrap}
.brand-mark{left:238px;top:50px;color:var(--white);font-weight:500;font-size:21px;letter-spacing:.3px;white-space:nowrap}
.access-card{position:absolute;left:160px;top:85px;width:217px;height:124px;background:var(--white);border:1px solid #b9c4de;box-shadow:0 1px 3px rgba(0,0,0,.25);overflow:hidden}
.access-card svg{position:absolute;left:0;top:0}
.card-name{position:absolute;left:84px;top:48px;color:var(--navy);font-weight:500;font-size:17px;white-space:nowrap}
.card-tap{position:absolute;left:128px;top:101px;color:var(--navy);font-size:6.5px;white-space:nowrap}
.nfc-badge{position:absolute;left:197px;top:10px;width:9px;height:9px;border:1.2px solid var(--navy);border-radius:1.5px}
.headline{left:0;width:396px;top:266px;text-align:center;color:var(--navy);font-size:70px;letter-spacing:-.5px;padding-right:40px;white-space:nowrap}
.subhead{left:0;width:396px;top:348px;text-align:center;font-size:22.5px;padding-right:40px;white-space:nowrap}
.subhead span{display:block;color:var(--navy);margin-top:2px}
.step{position:absolute;top:402px;width:124px;height:206px;background:var(--white);border-radius:9px;box-shadow:0 0 4px rgba(0,0,0,.18);overflow:hidden}
.step-1{left:7px}.step-2{left:134px}.step-3{left:265px;width:125px}
.step-label{height:40px;background:var(--navy);color:var(--white);font-size:22px;display:flex;align-items:center;justify-content:center;padding-top:3px}
.step-list{list-style:none;padding:14px 6px 0 24px}
.step-list li{position:relative;font-size:9px;line-height:10.6px;margin-bottom:6.5px}
.step-list li::before{content:"";position:absolute;left:-13px;top:1px;width:7px;height:7px;border-radius:50%;background:var(--navy)}
.step-list li::after{content:"";position:absolute;left:-11.2px;top:2.4px;width:2px;height:3.4px;border:solid var(--white);border-width:0 1.2px 1.2px 0;transform:rotate(40deg)}

/* back */
.back-photo{left:246px;top:6px;width:142px;height:235px;background:linear-gradient(180deg,#efe6dc 0%,#f3f3f3 40%,#dfe6f2 100%);border-radius:70px 70px 0 0}
.about-title{left:19px;top:14px;color:var(--white);font-size:36px;white-space:nowrap}
.about-by{left:19px;top:51px;color:var(--white);font-weight:500;font-size:12px;white-space:nowrap}
.about-copy{left:19px;top:71px;width:222px;color:var(--white);font-size:8.7px;line-height:14px}
.why-title{left:20px;top:254px;font-size:30px;color:#2b2b2b;white-space:nowrap}
.why-title span{color:var(--navy)}
.benefit{position:absolute;top:290px;width:120px;text-align:center}
.benefit-1{left:6px}.benefit-2{left:133px}.benefit-3{left:261px}
.benefit svg{display:block;margin:0 auto}
.benefit-name{font-size:15px;margin-top:6px;color:#1d1d1d}
.benefit-text{font-size:8.8px;line-height:11px;margin-top:2px}
.works-title{left:19px;top:451px;color:var(--white);font-size:31px}
.flow{position:absolute;left:0;top:0;width:396px;height:612px}
.flow-card{position:absolute;top:500px;width:70px;height:89px;background:var(--white);border-radius:7px;text-align:center;padding-top:2px}
.flow-num{font-weight:600;font-size:18px;line-height:22px;color:var(--navy-deep)}
.flow-name{font-size:11.5px;color:var(--navy);line-height:11px}
.flow-text{font-size:7.6px;line-height:9px;margin-top:5px;padding:0 3px}
.flow-1{left:13px}.flow-2{left:113px}.flow-3{left:213px}.flow-4{left:313px}
</style>
</head>
<body>

<!-- FRONT -->
<section class="page page--front" aria-label="Flyer front">
  <svg class="waves" viewBox="0 0 396 612" aria-hidden="true">
    <path fill="var(--wave)" d="M0 0H396V225C370 250 330 268 280 266C200 262 120 215 60 215C30 215 12 232 0 250Z"/>
    <path fill="var(--navy)" d="M0 0H396V205C365 240 320 255 270 255C200 253 130 205 70 200C40 198 15 206 0 215Z"/>
  </svg>
  <div class="photo front-photo" role="img" aria-label="Smiling female doctor in white coat with stethoscope, arms crossed"></div>
  <p class="abs head nfc-note">This card has the NFC access card.</p>
  <p class="abs brand-mark">Bright Path</p>

  <div class="access-card">
    <svg width="217" height="124" viewBox="0 0 217 124" role="img" aria-label="Card artwork: blue patterned panel">
      <path fill="var(--navy)" d="M0 0H92C78 20 58 40 60 70C62 95 50 110 52 124H0Z"/>
    </svg>
    <span class="nfc-badge" aria-hidden="true"></span>
    <p class="card-name">Bright Path</p>
    <p class="card-tap">Tap Here to Book</p>
    <svg class="abs" style="left:186px;top:98px" width="18" height="12" viewBox="0 0 18 12" aria-hidden="true">
      <rect x="1" y="1" width="10" height="10" rx="2" fill="none" stroke="var(--navy)" stroke-width="1"/>
      <path d="M13 3Q15 6 13 9M15 2Q18 6 15 10" fill="none" stroke="var(--navy)" stroke-width="1"/>
    </svg>
  </div>

  <h1 class="abs head headline">Need a Doctor?</h1>
  <h2 class="abs head subhead">How to book an appointment using<span>your Bright Path card</span></h2>

  <article class="step step-1">
    <h3 class="head step-label">Step 1</h3>
    <ul class="step-list">
      <li>Tap Your Card on Your Phone.</li>
      <li>Hold your card near the back of your phone.</li>
      <li>It will activate automatically — no app needed.</li>
      <li>The Bright Path scheduler will open.</li>
    </ul>
  </article>
  <article class="step step-2">
    <h3 class="head step-label">Step 2</h3>
    <ul class="step-list">
      <li>Schedule Your Appointment</li>
      <li>Select your clinical concern.</li>
      <li>Choose your time window.</li>
      <li>Register (only once). Confirm your appointment.</li>
    </ul>
  </article>
  <article class="step step-3">
    <h3 class="head step-label">Step 3</h3>
    <ul class="step-list">
      <li>Relax, we’ll take care of the rest</li>
      <li>A doctor will call during your scheduled time.</li>
      <li>Once booked, you’ll be able to call our office.</li>
      <li>No emails, no texts — just a real person.</li>
      <li>It’s that simple.</li>
    </ul>
  </article>
</section>

<!-- BACK -->
<section class="page page--back" aria-label="Flyer back">
  <svg class="waves" viewBox="0 0 396 612" aria-hidden="true">
    <path fill="var(--wave)" d="M0 0H396V205C375 228 345 242 300 243C230 243 150 195 80 195C45 195 20 215 0 235Z"/>
    <path fill="var(--navy)" d="M0 0H396V195C370 215 340 228 300 230C230 232 150 185 80 182C45 181 20 190 0 205Z"/>
    <path fill="var(--wave)" d="M0 612V445C20 415 60 400 110 405C190 412 260 450 320 445C360 441 385 425 396 410V612Z"/>
    <path fill="var(--navy)" d="M0 612V458C25 432 65 418 115 422C195 430 260 465 320 460C360 456 385 440 396 428V612Z"/>
  </svg>
  <div class="photo back-photo" role="img" aria-label="Smiling female doctor in white coat and blue scrubs with stethoscope"></div>
  <h2 class="abs head about-title">About Bright Path</h2>
  <p class="abs about-by">Created by Dr. Marcus Ferrigan</p>
  <p class="abs about-copy">Bright Path was founded to make healthcare simple and convenient. Prescription renewals. Common infections. Medical notes. And so much more. Our doctors can address 120+ health concerns virtually — providing quality care without the waiting room. No waiting rooms. Just real doctors providing real care.</p>

  <h2 class="abs head why-title">Why patients choose <span>Bright Path</span></h2>

  <div class="benefit benefit-1">
    <svg width="58" height="58" viewBox="0 0 58 58" aria-hidden="true">
      <circle cx="29" cy="29" r="28" fill="none" stroke="var(--navy)" stroke-width=".8" stroke-dasharray="1.5 1.5"/>
      <circle cx="29" cy="29" r="23" fill="var(--navy)"/>
      <rect x="19" y="19" width="20" height="15" rx="1.5" fill="none" stroke="#fff" stroke-width="1.4"/>
      <path d="M22 29l4-4 3 3 5-5" fill="none" stroke="#fff" stroke-width="1.4"/>
      <path d="M24 39h10" stroke="#fff" stroke-width="1.4"/>
    </svg>
    <h3 class="head benefit-name">Easy Access</h3>
    <p class="benefit-text">Book and Be Seen From Anywhere in BC.</p>
  </div>
  <div class="benefit benefit-2">
    <svg width="58" height="58" viewBox="0 0 58 58" aria-hidden="true">
      <circle cx="29" cy="29" r="28" fill="none" stroke="var(--navy)" stroke-width=".8" stroke-dasharray="1.5 1.5"/>
      <circle cx="29" cy="29" r="23" fill="var(--navy)"/>
      <rect x="22" y="16" width="14" height="25" rx="2" fill="none" stroke="#fff" stroke-width="1.4"/>
      <path d="M27 38h4" stroke="#fff" stroke-width="1.4"/>
      <path d="M30 27l6 6-2 4" fill="none" stroke="#fff" stroke-width="1.4"/>
    </svg>
    <h3 class="head benefit-name">Effortless<br>Booking</h3>
    <p class="benefit-text">Tap your Bright Path Card to Begin.</p>
  </div>
  <div class="benefit benefit-3">
    <svg width="58" height="58" viewBox="0 0 58 58" aria-hidden="true">
      <circle cx="29" cy="29" r="28" fill="none" stroke="var(--navy)" stroke-width=".8" stroke-dasharray="1.5 1.5"/>
      <circle cx="29" cy="29" r="23" fill="var(--navy)"/>
      <circle cx="29" cy="19" r="3.5" fill="none" stroke="#fff" stroke-width="1.3"/>
      <path d="M27.5 19l1 1 2-2" fill="none" stroke="#fff" stroke-width="1"/>
      <circle cx="21" cy="28" r="3" fill="none" stroke="#fff" stroke-width="1.3"/>
      <circle cx="37" cy="28" r="3" fill="none" stroke="#fff" stroke-width="1.3"/>
      <circle cx="29" cy="30" r="3" fill="none" stroke="#fff" stroke-width="1.3"/>
      <path d="M16 38q5-7 10 0M32 38q5-7 10 0M24 41q5-7 10 0" fill="none" stroke="#fff" stroke-width="1.3"/>
    </svg>
    <h3 class="head benefit-name">Trusted<br>Physicians</h3>
    <p class="benefit-text">Every visit is with a Licensed BC Family Doctor.</p>
  </div>

  <h2 class="abs head works-title">How it works</h2>
  <svg class="flow" viewBox="0 0 396 612" aria-hidden="true">
    <g stroke="#ffffff" stroke-width="1" stroke-dasharray="2 2" fill="none">
      <rect x="6" y="493" width="83" height="103" rx="9"/>
      <rect x="106" y="493" width="83" height="103" rx="9"/>
      <rect x="206" y="493" width="83" height="103" rx="9"/>
      <rect x="306" y="493" width="83" height="103" rx="9"/>
    </g>
    <rect x="6" y="520" width="83" height="76" rx="9" fill="var(--ice)"/>
    <rect x="106" y="520" width="83" height="76" rx="9" fill="var(--grey-box)"/>
    <rect x="206" y="520" width="83" height="76" rx="9" fill="var(--ice)"/>
    <rect x="306" y="520" width="83" height="76" rx="9" fill="var(--grey-box)"/>
    <g stroke="var(--ice)" stroke-width="1.2">
      <path d="M89 530H106M189 530H206M289 530H306"/>
    </g>
    <g fill="var(--ice)" stroke="var(--navy)" stroke-width="1">
      <circle cx="89" cy="530" r="3"/><circle cx="106" cy="530" r="3"/><circle cx="97.5" cy="530" r="3"/>
      <circle cx="189" cy="530" r="3"/><circle cx="206" cy="530" r="3"/><circle cx="197.5" cy="530" r="3"/>
      <circle cx="289" cy="530" r="3"/><circle cx="306" cy="530" r="3"/><circle cx="297.5" cy="530" r="3"/>
    </g>
  </svg>
  <div class="flow-card flow-1">
    <p class="flow-num">1</p>
    <h3 class="head flow-name">Book your<br>visit</h3>
    <p class="flow-text">choose a time window that fits your day.</p>
  </div>
  <div class="flow-card flow-2">
    <p class="flow-num">2</p>
    <h3 class="head flow-name">Join the<br>queue</h3>
    <p class="flow-text">you’ll be called when it’s your turn.</p>
  </div>
  <div class="flow-card flow-3">
    <p class="flow-num">3</p>
    <h3 class="head flow-name">Speak directly<br>with your<br>doctor</h3>
    <p class="flow-text">simple, secure, and stress-free.</p>
  </div>
  <div class="flow-card flow-4">
    <p class="flow-num">4</p>
    <h3 class="head flow-name">Convenient<br>care for<br>common<br>concerns</h3>
  </div>
</section>

</body>
</html>
```